I would like a site similar to this: http://www.givewheelsforheroes.example

old site: http://www.autosforpatriots.example

Create a professional website; a car donation site seeking leads to return calls.

Please see http://www.givewheelsforheroes.example for the concept I am after.

The webpage should have a professional feel. The pages to include are 'Home', 'About us' and 'Get Started'

Industry/Entity Type

It Professional

Coding

Coded - Design and coding required

Number of Pages Required

1 page

```html
<!DOCTYPE html>
<html lang="en">
<head>
<meta charset="utf-8">
<title>Autos for Patriots – Car Donation</title>
<link href="https://fonts.googleapis.com/css2?family=Roboto+Slab:wght@400;700&family=Open+Sans:wght@400;600;700&display=swap" rel="stylesheet">
<style>
:root{
  --blue:#1a4fa0;
  --blue-dark:#15438a;
  --blue-top:#2a6fd0;
  --red:#b5150f;
  --red-dark:#a8120c;
  --ink:#555;
  --muted:#777;
  --light:#f4f5f7;
  --footer-bar:#474747;
  --btn:#2c2c2c;
}
*{box-sizing:border-box;margin:0;padding:0}
html,body{width:694px;height:1200px;overflow:hidden}
body{position:relative;background:#fff;font-family:"Open Sans",Arial,sans-serif;color:var(--ink)}
.abs{position:absolute}
.slab{font-family:"Roboto Slab",Georgia,serif}

/* header */
.topbar{left:0;top:0;width:694px;height:67px;background:linear-gradient(180deg,#3a7fdc 0%,#2567c6 60%,#1f5cb8 100%)}
.brand{left:52px;top:26px;display:flex;align-items:center;gap:6px;color:#fff;font-family:"Roboto Slab",serif;font-size:13px}
.brand-mark{width:14px;height:14px;background:var(--red)}
.nav{left:0;top:67px;width:694px;height:28px;background:var(--blue-dark);display:flex;align-items:center}
.nav a{color:#fff;text-decoration:none;font-family:"Roboto Slab",serif;font-size:7.4px;position:absolute;top:10px}

/* hero */
.hero{left:0;top:95px;width:694px;height:221px;background:linear-gradient(110deg,#f0b04a 0%,#e07a3a 18%,#6a4a52 40%,#3b3236 62%,#1e1c22 100%)}

/* form panel */
.panel{left:459px;top:8px;width:186px;height:282px;background:var(--red)}
.panel-head{left:459px;top:8px;width:186px;height:59px;background:var(--red-dark)}
.call-label{left:459px;top:30px;width:186px;text-align:center;color:#fff;font-family:"Roboto Slab",serif;font-size:10.5px;letter-spacing:.3px}
.call-number{left:459px;top:46px;width:186px;text-align:center;color:#fff;font-family:"Roboto Slab",serif;font-size:14px;font-weight:700}
.form-title{left:459px;top:73px;width:186px;text-align:center;color:#fff;font-family:"Roboto Slab",serif;font-size:11.5px}
.field{background:#fff;border-radius:2px;font-size:6.4px;color:#555;padding:0 8px;display:flex;align-items:center}
.donate-btn{left:469px;top:245px;width:166px;height:23px;background:var(--btn);color:#fff;font-size:7.6px;font-weight:600;display:flex;align-items:center;justify-content:center;border-radius:2px;letter-spacing:.2px}

/* sections */
.section-title{width:694px;text-align:center;font-family:"Roboto Slab",serif;font-size:13px;color:#555}
.section-lead{width:694px;text-align:center;font-size:6.4px;line-height:13.6px;color:#777}

.step-icon{width:48px;height:48px;border-radius:50%;border:1px solid currentColor;display:flex;align-items:center;justify-content:center}
.step-title{font-family:"Roboto Slab",serif;font-size:10px}
.step-text{font-size:6.4px;line-height:14.4px;color:#777;width:130px}
.blue{color:var(--blue)}
.red{color:var(--red)}

.why{left:0;top:530px;width:694px;height:216px;background:var(--blue)}
.why-red{left:0;top:530px;width:694px;height:216px;background:var(--red);clip-path:polygon(368px 0,694px 0,694px 216px,314px 216px)}
.why h2{font-family:"Roboto Slab",serif;font-weight:400;font-size:11.5px;color:#fff}
.why-item h3{font-family:"Roboto Slab",serif;font-weight:400;font-size:8.6px;color:#fff;letter-spacing:.1px}
.why-item p{font-size:5.6px;line-height:10.5px;color:#9fb6de;margin-top:3px;width:230px}
.donate-copy{left:388px;top:573px;width:260px;font-size:6.5px;line-height:13.4px;color:#fff}
.check{display:flex;align-items:center;gap:9px;font-size:6.4px;color:#fff}

.prog-icon{width:68px;height:68px;border-radius:50%;display:flex;align-items:center;justify-content:center;box-shadow:0 0 0 1.5px #fff,0 0 0 2.5px currentColor}
.prog-title{width:150px;text-align:center;font-family:"Roboto Slab",serif;font-size:9.6px}
.prog-text{width:150px;text-align:center;font-size:6.3px;line-height:13.6px;color:#777}
.read-more{width:150px;text-align:center;font-family:"Roboto Slab",serif;font-size:6.6px;font-weight:700;text-decoration:underline}

/* footer */
.footer{left:0;top:1010px;width:694px;height:152px;background:var(--light)}
.foot-head{font-size:8.6px;font-weight:600;color:#444;letter-spacing:.2px}
.contact-line{display:flex;align-items:flex-start;gap:8px;font-size:6.3px;color:#666;line-height:9px}
.news-input{left:377px;top:1089px;width:122px;height:19px;background:#fff;border:1px solid #ddd;font-size:6.4px;color:#555;padding-left:8px;display:flex;align-items:center}
.subscribe{left:377px;top:1118px;width:47px;height:15px;background:var(--red);color:#fff;font-size:5.6px;font-weight:700;display:flex;align-items:center;justify-content:center}
.social{width:20px;height:20px;border-radius:50%;border:1px solid #c8c8c8}
.copyright{left:0;top:1162px;width:694px;height:38px;background:var(--footer-bar);color:#fff;font-size:6.8px;text-align:center;line-height:38px}
</style>
</head>
<body>

<header>
  <div class="abs topbar"></div>
  <div class="abs brand"><span class="brand-mark"></span>Autos for Patriots</div>
  <nav class="abs nav">
    <a style="left:70px">HOME</a>
    <a style="left:120px">ABOUT US</a>
    <a style="left:184px">SERVICES</a>
    <a style="left:249px">HOW IT WORKS</a>
    <a style="left:333px">CHARITIES</a>
    <a style="left:400px">CONTACT US</a>
  </nav>
</header>

<div class="abs hero" role="img" aria-label="Photo of a silver car parked on an open road at sunset"></div>

<aside>
  <div class="abs panel"></div>
  <div class="abs panel-head"></div>
  <svg class="abs" style="left:459px;top:8px" width="186" height="12" aria-hidden="true"><polygon points="0,0 93,8 186,0" fill="#9e110b"/></svg>
  <div class="abs call-label">CALL TODAY TO DONATE</div>
  <div class="abs call-number">1-800-555-0142</div>
  <div class="abs form-title">Donation Pick Up Form</div>
  <div class="abs field" style="left:469px;top:108px;width:81px;height:20px">First Name :</div>
  <div class="abs field" style="left:554px;top:108px;width:81px;height:20px">Last Name :</div>
  <div class="abs field" style="left:469px;top:133px;width:166px;height:21px">Email :</div>
  <div class="abs field" style="left:469px;top:158px;width:166px;height:21px">Phone :</div>
  <div class="abs field" style="left:469px;top:184px;width:81px;height:21px">Zip Code :</div>
  <div class="abs field" style="left:554px;top:184px;width:81px;height:21px">Year of Vehicle :</div>
  <div class="abs field" style="left:469px;top:211px;width:81px;height:21px">Make of Vehicle :</div>
  <div class="abs field" style="left:554px;top:211px;width:81px;height:21px">Model of Vehicle :</div>
  <div class="abs donate-btn">CLICK TO DONATE YOUR CAR</div>
</aside>

<section>
  <h2 class="abs section-title" style="left:0;top:339px;font-weight:400">How It Works</h2>
  <p class="abs section-lead" style="left:0;top:362px">Sed ut perspiciatis unde omnis iste natus error sit voluptatem accusantium doloremque laudantium, totam rem aperiam ab<br>illo inventore veritatis et quasi architecto beatae vitae dicta sunt explicabo.</p>

  <div class="abs step-icon blue" style="left:50px;top:422px">
    <svg width="22" height="22" viewBox="0 0 24 24"><path d="M3 8c0-3 4-4 9-4s9 1 9 4v2h-5V8H8v2H3z" fill="#1a4fa0"/><path d="M6 12h12l2 8H4z" fill="#1a4fa0"/><g fill="#fff"><circle cx="10" cy="15" r="1"/><circle cx="12" cy="15" r="1"/><circle cx="14" cy="15" r="1"/><circle cx="10" cy="17.5" r="1"/><circle cx="12" cy="17.5" r="1"/><circle cx="14" cy="17.5" r="1"/></g></svg>
  </div>
  <h3 class="abs step-title blue" style="left:110px;top:419px;font-weight:400">Call Us</h3>
  <p class="abs step-text" style="left:110px;top:439px">We issue you an IRS tax receipt &amp; offer the largest resale network to get you the highest tax write-off possible</p>

  <div class="abs step-icon red" style="left:254px;top:422px">
    <svg width="26" height="22" viewBox="0 0 26 22"><path d="M2 11h8l3-5h5v10H2z" fill="#b5150f"/><path d="M18 4l6-3v3M24 4v6" stroke="#b5150f" stroke-width="1.6" fill="none"/><circle cx="6" cy="17" r="3" fill="#b5150f" stroke="#fff" stroke-width="1"/><circle cx="16" cy="17" r="3" fill="#b5150f" stroke="#fff" stroke-width="1"/></svg>
  </div>
  <h3 class="abs step-title red" style="left:315px;top:419px;font-weight:400">We Tow It</h3>
  <p class="abs step-text" style="left:315px;top:439px">We issue you an IRS tax receipt &amp; offer the largest resale network to get you the highest tax write-off possible</p>

  <div class="abs step-icon blue" style="left:459px;top:422px;font-family:'Roboto Slab',serif;font-size:22px;font-weight:700">%</div>
  <h3 class="abs step-title blue" style="left:520px;top:419px;font-weight:400">Tax Write Off</h3>
  <p class="abs step-text" style="left:520px;top:439px">We issue you an IRS tax receipt &amp; offer the largest resale network to get you the highest tax write-off possible</p>
</section>

<section>
  <div class="abs why"></div>
  <div class="abs why why-red" style="background:var(--red)"></div>
  <div class="abs why" style="background:none;height:0">
    <h2 class="abs" style="left:51px;top:18px;white-space:nowrap">Why Donate Your Car to Us?</h2>
    <div class="abs why-item" style="left:50px;top:47px"><h3>FREE LOCAL TOWING TO YOU</h3><p>We will pick up your car donation, running or not, when it's most convenient, at home or work.</p></div>
    <div class="abs why-item" style="left:50px;top:86px"><h3>ALL CARS ACCEPTED</h3><p>We take your car regardless of its condition or registration status.</p></div>
    <div class="abs why-item" style="left:50px;top:127px"><h3>INCOME TAX DEDUCTION</h3><p>We issue you an IRS tax receipt &amp; offer the largest resale network to get you the highest tax write-off possible.</p></div>
    <div class="abs why-item" style="left:50px;top:176px"><h3>IRS 501(C)3 APPROVED</h3><p>Free 24/7 Pickup with No DMV Hassles.</p></div>
    <h2 class="abs" style="left:388px;top:18px;white-space:nowrap">Donate Your Car Today!</h2>
  </div>
  <p class="abs donate-copy">Sed ut perspiciatis unde omnis iste natus error sit voluptatem accusantium dolore mque laudantium, totam rem aperiam, eaque ipsa quae ab illo inventore veritatis et quasi architecto beatae vitae dicta sunt explicabo.</p>
  <div class="abs" style="left:387px;top:628px;display:flex;flex-direction:column;gap:11.2px">
    <div class="check"><svg width="8" height="8" viewBox="0 0 10 10"><circle cx="5" cy="5" r="4" fill="none" stroke="#fff" stroke-width="1.2"/><path d="M3 5l1.5 1.5L7 3.6" stroke="#fff" stroke-width="1.2" fill="none"/></svg>You have no costs.</div>
    <div class="check"><svg width="8" height="8" viewBox="0 0 10 10"><circle cx="5" cy="5" r="4" fill="none" stroke="#fff" stroke-width="1.2"/><path d="M3 5l1.5 1.5L7 3.6" stroke="#fff" stroke-width="1.2" fill="none"/></svg>Free towing, running or not.</div>
    <div class="check"><svg width="8" height="8" viewBox="0 0 10 10"><circle cx="5" cy="5" r="4" fill="none" stroke="#fff" stroke-width="1.2"/><path d="M3 5l1.5 1.5L7 3.6" stroke="#fff" stroke-width="1.2" fill="none"/></svg>We issue you an IRS tax receipt.</div>
    <div class="check"><svg width="8" height="8" viewBox="0 0 10 10"><circle cx="5" cy="5" r="4" fill="none" stroke="#fff" stroke-width="1.2"/><path d="M3 5l1.5 1.5L7 3.6" stroke="#fff" stroke-width="1.2" fill="none"/></svg>We take care of all paperwork.</div>
    <div class="check"><svg width="8" height="8" viewBox="0 0 10 10"><circle cx="5" cy="5" r="4" fill="none" stroke="#fff" stroke-width="1.2"/><path d="M3 5l1.5 1.5L7 3.6" stroke="#fff" stroke-width="1.2" fill="none"/></svg>And we take care of DMV &amp; Smog issues.</div>
  </div>
</section>

<section>
  <h2 class="abs section-title" style="left:0;top:768px;font-weight:400">Car Donation Program</h2>
  <p class="abs section-lead" style="left:0;top:791px">Sed ut perspiciatis unde omnis iste natus error sit voluptatem accusantium doloremque laudantium, totam rem aperiam ab<br>illo inventore veritatis et quasi architecto beatae vitae dicta sunt explicabo.</p>

  <div class="abs prog-icon blue" style="left:88px;top:840px;background:var(--blue)">
    <svg width="36" height="36" viewBox="0 0 36 36"><path d="M18 20s-8-5-8-10a4 4 0 0 1 8-1 4 4 0 0 1 8 1c0 5-8 10-8 10z" fill="#fff"/><path d="M4 16l6 10 5 4M32 16l-6 10-5 4" stroke="#fff" stroke-width="2.4" fill="none" stroke-linecap="round"/></svg>
  </div>
  <div class="abs prog-icon red" style="left:239px;top:840px;background:var(--red)">
    <svg width="40" height="24" viewBox="0 0 40 24"><path d="M3 15l3-7h5l4-5h12l5 6h4l1 6z" fill="#fff"/><rect x="2" y="14" width="36" height="5" rx="2" fill="#fff"/><circle cx="10" cy="19" r="3.5" fill="#b5150f" stroke="#fff" stroke-width="1.5"/><circle cx="30" cy="19" r="3.5" fill="#b5150f" stroke="#fff" stroke-width="1.5"/></svg>
  </div>
  <div class="abs prog-icon blue" style="left:389px;top:840px;background:var(--blue)">
    <svg width="28" height="34" viewBox="0 0 28 34"><path d="M3 2h16l6 6v24H3z" fill="none" stroke="#fff" stroke-width="2.4"/><path d="M8 11h10M8 16h12M8 21h6" stroke="#fff" stroke-width="2"/><text x="15" y="29" font-family="Open Sans,sans-serif" font-size="10" font-weight="700" fill="#fff">$</text></svg>
  </div>
  <div class="abs prog-icon red" style="left:540px;top:840px;background:var(--red)">
    <svg width="40" height="34" viewBox="0 0 40 34"><path d="M3 22h12l5-8h7v14H3z" fill="#fff"/><path d="M27 10l8-6M35 4v10" stroke="#fff" stroke-width="2.4" fill="none"/><path d="M33 14a2 2 0 1 1 -2 2" stroke="#fff" stroke-width="2" fill="none"/><circle cx="9" cy="28" r="4" fill="#b5150f" stroke="#fff" stroke-width="2"/><circle cx="23" cy="28" r="4" fill="#b5150f" stroke="#fff" stroke-width="2"/></svg>
  </div>

  <h3 class="abs prog-title blue" style="left:47px;top:913px;font-weight:400">Donations Accepted</h3>
  <h3 class="abs prog-title red" style="left:197px;top:913px;font-weight:400">All Vehicle Type</h3>
  <h3 class="abs prog-title blue" style="left:347px;top:913px;font-weight:400">Tax Deductible</h3>
  <h3 class="abs prog-title red" style="left:498px;top:913px;font-weight:400">Towing Free</h3>

  <p class="abs prog-text" style="left:47px;top:932px">Sed ut perspiciatis unde omnis iste natus beatae vitae dicta sunt explicabo.</p>
  <p class="abs prog-text" style="left:197px;top:932px">Sed ut perspiciatis unde omnis iste natus beatae vitae dicta sunt explicabo.</p>
  <p class="abs prog-text" style="left:347px;top:932px">Sed ut perspiciatis unde omnis iste natus beatae vitae dicta sunt explicabo.</p>
  <p class="abs prog-text" style="left:498px;top:932px">Sed ut perspiciatis unde omnis iste natus beatae vitae dicta sunt explicabo.</p>

  <a class="abs read-more blue" style="left:47px;top:966px">READ MORE</a>
  <a class="abs read-more red" style="left:197px;top:966px">READ MORE</a>
  <a class="abs read-more blue" style="left:347px;top:966px">READ MORE</a>
  <a class="abs read-more red" style="left:498px;top:966px">READ MORE</a>
</section>

<footer>
  <div class="abs footer"></div>
  <h4 class="abs foot-head" style="left:57px;top:1036px">SAFE &amp; SECURE</h4>
  <div class="abs" style="left:52px;top:1064px;width:84px;height:32px;background:#d9dce2;border-radius:3px"></div>
  <div class="abs" style="left:150px;top:1063px;width:38px;height:34px;border-radius:50%;border:2px solid #3b8fc6;background:#e9f2f8"></div>

  <h4 class="abs foot-head" style="left:218px;top:1036px">CONTACT US</h4>
  <div class="abs" style="left:218px;top:1063px;display:flex;flex-direction:column;gap:7.8px">
    <div class="contact-line"><svg width="8" height="8" viewBox="0 0 10 10"><path d="M1 3c0-1.5 2-2 4-2s4 .5 4 2v1H7V3H3v1H1zM2 5h6l1 4H1z" fill="#888"/></svg>1-800-555-0142 (Phone)</div>
    <div class="contact-line"><svg width="8" height="8" viewBox="0 0 10 10"><rect x="2.5" y="1" width="5" height="3" fill="#888"/><rect x="1" y="4" width="8" height="4" fill="#888"/><rect x="2.5" y="7" width="5" height="2" fill="#bbb"/></svg>1-800-555-0143 (Fax)</div>
    <div class="contact-line"><svg width="8" height="8" viewBox="0 0 10 10"><rect x="1" y="2" width="8" height="6" fill="#888"/><path d="M1 2l4 3 4-3" stroke="#fff" stroke-width=".8" fill="none"/></svg><span style="text-decoration:underline">info@autosforpatriots.example</span></div>
    <div class="contact-line"><svg width="8" height="8" viewBox="0 0 10 10"><path d="M5 9C3 6.5 2 5 2 3.6a3 3 0 0 1 6 0C8 5 7 6.5 5 9z" fill="#888"/><circle cx="5" cy="3.6" r="1" fill="#fff"/></svg><span>AFP 3350 lorem ipsum Dummy<br>Text Lorem Ipsum</span></div>
  </div>

  <h4 class="abs foot-head" style="left:377px;top:1036px">NEWSLETTER</h4>
  <p class="abs" style="left:377px;top:1060px;width:130px;font-size:6.4px;line-height:11px;color:#777">Register Your email address to get information about us</p>
  <div class="abs news-input">Email Address</div>
  <div class="abs subscribe">SUBSCRIBE</div>

  <h4 class="abs foot-head" style="left:524px;top:1037px">FOLLOW US</h4>
  <p class="abs" style="left:524px;top:1062px;width:130px;font-size:5.8px;line-height:11px;color:#777">Lorem ipsum dolor sit amet, conse ctetur adipiscing elit. Nulla in purus nibh. Donec ornare</p>
  <div class="abs" style="left:523px;top:1105px;display:flex;gap:5px">
    <div class="social"></div><div class="social"></div><div class="social"></div><div class="social"></div><div class="social"></div>
  </div>

  <div class="abs copyright">© Copyright 2017 Autos for Patriots.All Rights Reserved</div>
</footer>

</body>
</html>
```